Business card for dental office
Quillbrook Ridge Dental Care
Bright & Fun-filled
18 Larkspur Ln, Suite 310
Fernhollow, CO 89777
quillbrookridgedentalcare@postmerro.com
quillbrookridgedentalcare.com
Please include website on business card but do not include email address.

```html
<!DOCTYPE html>
<html lang="en">
<head>
<meta charset="utf-8">
<title>Quillbrook Ridge Dental Care – Business Card</title>
<link rel="stylesheet" href="https://fonts.googleapis.com/css2?family=Cinzel:wght@400;600&display=swap">
<style>
  :root {
    --page-bg: #e9eaec;
    --brand-blue: #2b9be0;
    --brand-blue-deep: #1679c2;
    --brand-tan: #a88a73;
    --card-white: #ffffff;
    --ink-blue: #1f86cf;
    --ink-grey: #7d8790;
  }
  * { margin: 0; padding: 0; box-sizing: border-box; }
  html, body { width: 1200px; height: 984px; overflow: hidden; }
  body {
    background: var(--page-bg);
    font-family: "Cinzel", "Times New Roman", serif;
    position: relative;
  }
  .card {
    position: absolute;
    left: 250px;
    width: 700px;
    height: 400px;
    border-radius: 26px;
    overflow: hidden;
    box-shadow: 0 10px 28px rgba(0,0,0,0.18);
  }
  /* back side */
  .card-back {
    top: 52px;
    background: radial-gradient(ellipse at 55% 40%, #5cbaf0 0%, var(--brand-blue) 55%, var(--brand-blue-deep) 100%);
    color: var(--card-white);
  }
  .card-back .website {
    position: absolute;
    left: 0; right: 0; top: 140px;
    text-align: center;
    font-size: 14px;
    letter-spacing: 4px;
    color: var(--card-white);
  }
  .card-back .brand-name {
    position: absolute;
    left: 0; right: 0; top: 190px;
    text-align: center;
    font-size: 30px;
    font-weight: 600;
    letter-spacing: 3px;
    color: var(--card-white);
  }
  /* front side */
  .card-front {
    top: 512px;
    background: var(--card-white);
  }
  .card-front .swoosh {
    position: absolute;
    left: 0; top: 0;
    width: 700px; height: 400px;
  }
  .card-front .brand-name {
    position: absolute;
    left: 260px; top: 50px;
    width: 360px;
    text-align: center;
    font-size: 24px;
    line-height: 32px;
    font-weight: 600;
    letter-spacing: 2px;
    color: var(--ink-blue);
  }
  .card-front .brand-mark {
    display: block;
    width: 14px; height: 14px;
    margin: 0 auto 8px;
    border-radius: 50%;
    background: var(--brand-blue);
  }
  .card-front .office-name {
    position: absolute;
    left: 265px; top: 180px;
    font-size: 17px;
    line-height: 24px;
    color: var(--ink-blue);
  }
  .contact-list {
    position: absolute;
    left: 400px; top: 268px;
    list-style: none;
    font-size: 11px;
    line-height: 17px;
    color: var(--ink-grey);
    letter-spacing: 0.5px;
  }
  .contact-list li { display: flex; align-items: center; gap: 7px; }
  .contact-list .dot {
    width: 10px; height: 10px;
    border-radius: 50%;
    background: var(--brand-blue);
    flex: none;
  }
  .contact-list .spacer { visibility: hidden; }
</style>
</head>
<body>

  <section class="card card-back" aria-label="Card back">
    <div class="website">www.quillbrookridgedentalcare.com</div>
    <div class="brand-name">Quillbrook Ridge Dental Care</div>
  </section>

  <section class="card card-front" aria-label="Card front">
    <svg class="swoosh" viewBox="0 0 700 400" aria-hidden="true">
      <path d="M0 0 H210 C120 90 95 250 150 400 H0 Z" fill="var(--brand-blue)"/>
      <path d="M185 400 C140 280 150 140 240 40 C175 150 170 280 215 400 Z" fill="var(--brand-tan)"/>
    </svg>

    <div class="brand-name">
      <span class="brand-mark"></span>
      Quillbrook Ridge<br>Dental Care
    </div>

    <div class="office-name">Quillbrook Ridge<br>Dental Care</div>

    <ul class="contact-list">
      <li><span class="dot"></span>18 Larkspur Ln, Suite 310</li>
      <li><span class="dot spacer"></span>Fernhollow, CO 89777</li>
      <li><span class="dot"></span>(555) 555-0148</li>
      <li><span class="dot"></span>(555) 555-0162</li>
      <li><span class="dot"></span>www.quillbrookridgedentalcare.com</li>
    </ul>
  </section>

</body>
</html>
```